KA VERLINE

We need a letterhead design for an Image & Etiquette Consultancy company based in Singapore.

The services we provide are Personal Image Consultation, Image & Etiquette Workshop for schools and corporate.

The design should have our corporate colour as seen in the logo files I have uploaded.

Since our company helps clients with their image, the design should be aesthetically very appealing. It should reflect a very classy & elegant feel.

I will print the letterhead using my printer but most of the time will use it to write letters to my clients therefore the format should include MS Word.

```html
<!DOCTYPE html>
<html lang="en">
<head>
<meta charset="utf-8">
<title>KA VERLINE Letterhead</title>
<link rel="stylesheet" href="https://fonts.googleapis.com/css2?family=Source+Sans+3:wght@300;400&family=Open+Sans:wght@400&display=swap">
<style>
  :root {
    --backdrop: #e2e2e2;
    --paper: #eceef0;
    --gold-deep: #c49131;
    --gold-bright: #efc01a;
    --gold-pale: #fff8d2;
    --brand-purple: #2a0f3e;
    --ink: #1c1c1c;
    --signature-tone: #c9d1e3;
  }
  html, body {
    margin: 0;
    padding: 0;
    width: 1113px;
    height: 1200px;
    overflow: hidden;
    background: var(--backdrop);
  }
  .letterhead {
    position: absolute;
    left: 198px;
    top: 94px;
    width: 716px;
    height: 1012px;
    background: var(--paper);
    font-family: "Source Sans 3", sans-serif;
    color: var(--ink);
  }
  .frame-side {
    position: absolute;
    top: 0;
    width: 27px;
    height: 100%;
    background: linear-gradient(to bottom,
      var(--gold-deep) 0%,
      var(--gold-deep) 8%,
      var(--gold-bright) 22%,
      var(--gold-pale) 49%,
      var(--gold-bright) 77%,
      var(--gold-deep) 92%,
      var(--gold-deep) 100%);
  }
  .frame-side--left { left: 0; }
  .frame-side--right { right: 0; }
  .frame-corner {
    position: absolute;
    width: 108px;
    background: var(--gold-deep);
  }
  .frame-corner--top { top: 0; height: 28px; }
  .frame-corner--bottom { bottom: 0; height: 31px; }
  .frame-corner--left { left: 0; }
  .frame-corner--right { right: 0; }
  .brand-name {
    position: absolute;
    top: 28px;
    left: 0;
    width: 100%;
    text-align: center;
    font-size: 52px;
    font-weight: 300;
    letter-spacing: 2px;
    color: var(--brand-purple);
    line-height: 1;
    margin: 0;
  }
  .letter-body {
    position: absolute;
    left: 82px;
    top: 210px;
    width: 543px;
  }
  .salutation {
    font-size: 22px;
    margin: 0 0 44px;
    font-weight: 400;
  }
  .letter-body p.paragraph {
    font-size: 13px;
    line-height: 19.8px;
    text-align: justify;
    margin: 0 0 19.8px;
  }
  .closing {
    position: absolute;
    left: 549px;
    top: 654px;
    font-size: 13px;
    margin: 0;
  }
  .signature {
    position: absolute;
    left: 455px;
    top: 686px;
    width: 157px;
    height: 62px;
    background: var(--signature-tone);
    border-radius: 4px;
  }
  .contact {
    position: absolute;
    left: 0;
    top: 935px;
    width: 100%;
    text-align: center;
    font-family: "Open Sans", sans-serif;
    font-size: 13.5px;
    line-height: 21px;
    margin: 0;
  }
</style>
</head>
<body>
  <main class="letterhead">
    <div class="frame-side frame-side--left"></div>
    <div class="frame-side frame-side--right"></div>
    <div class="frame-corner frame-corner--top frame-corner--left"></div>
    <div class="frame-corner frame-corner--top frame-corner--right"></div>
    <div class="frame-corner frame-corner--bottom frame-corner--left"></div>
    <div class="frame-corner frame-corner--bottom frame-corner--right"></div>

    <h1 class="brand-name">KA VERLINE</h1>

    <section class="letter-body">
      <p class="salutation">Dear Mr. Harlow,</p>
      <p class="paragraph">Lorem ipsum dolor sit amet, consectetur adipiscing elit. Donec orci purus, luctus vitae dignissim eu, iaculis sed purus. Vivamus faucibus, ipsum nec aliquet viverra, leo mauris condimentum ligula, sit amet sagittis enim ligula quis arcu. Nam egestas tortor id nisi porttitor mattis. In tortor ante, ultricies in suscipit a, tempus non massa. Vivamus et auctor mi. Fusce vel massa nulla. Phasellus nec eros mauris, et scelerisque orci.</p>
      <p class="paragraph">Donec malesuada orci vitae nulla accumsan porta a id massa. Quisque accumsan iaculis magna sit amet fringilla. Maecenas consequat, magna eget tincidunt semper, odio nibh rutrum mi, id feugiat ante nisi eu risus. Vestibulum nunc orci, rhoncus a placerat in, ultricies in mi. Cras mattis varius eros, vel fringilla nisi suscipit eget. Quisque scelerisque sagittis nulla at porttitor.</p>
      <p class="paragraph">Sed id augue vitae urna euismod commodo aliquet a quam. Pellentesque arcu velit, cursus et malesuada ut, consequat et diam. Nullam erat sem, rhoncus id ullamcorper vitae, rhoncus et arcu. In ultricies ultricies nulla, ut rutrum nisi iaculis at. Donec eu magna a metus ornare faucibus. Fusce aliquet faucibus ultricies. Morbi semper, est id tincidunt gravida, sem arcu adipiscing lacus, ac bibendum nulla leo eu purus. Quisque nec diam sed risus consectetur a ccumsan quis quis nibh. Vestibulum id purus lorem.</p>
    </section>

    <p class="closing">Sincerely,</p>
    <div class="signature" role="img" aria-label="Handwritten signature of Evan Marsh"></div>

    <p class="contact">
      Web: kaverline-example.com<br>
      Email: hello@kaverline-example.com<br>
      Tell: 555 0142
    </p>
  </main>
</body>
</html>
```